High Quality Business card for Property Management Agency - Super Classy and professional design

High Quality Business card design.

We need a business card designed for our Property Management Agency.
We are located on Sydney's Northern Beaches and manage beautiful properties along the beach and harbor.
We need a design that oozes modern, classy and professional.
I would like it to be double sided with contact details and logo on the front and just the logo on the back.

I need a print ready PDF version of the file as well as an editable photoshop (PSD) version of the file.

Logo and information details attached.

Target Market(s)

Property owners/investors, Male and Female Aged 28-65

Industry/Entity Type

Real Estate

Contact Information for Business Card

Tom Carrick
Tel: 0467 239 018
Email: tom@harvestlaneestates.com.au
Website: www.harvestlaneestates.com.au
Address: Level 2, 17 Wattlecourt Rd, Dunmarra NSW 2187

Font styles to use
Sans Serif

Requirements
Must have
• - Logo front and back
• - Business card details listed above and attached
• - Colour
Nice to have
• Sleek and professional

```html
<!DOCTYPE html>
<html lang="en">
<head>
<meta charset="utf-8">
<title>Harvest Lane Estates – Business Card</title>
<link rel="stylesheet" href="https://fonts.googleapis.com/css2?family=Source+Sans+3:wght@400;600;700&display=swap">
<style>
  :root {
    --stage: #1c1d1f;
    --card-dark: #141617;
    --card-light: #ffffff;
    --ink: #1a1a1a;
    --teal: #1e8a94;
    --white: #ffffff;
  }
  * { box-sizing: border-box; margin: 0; padding: 0; }
  html, body {
    width: 1200px; height: 900px; overflow: hidden;
    background: var(--stage);
    font-family: "Source Sans 3", sans-serif;
  }
  .canvas { position: relative; width: 1200px; height: 900px; }

  .card {
    position: absolute;
    width: 540px; height: 330px;
    box-shadow: 0 14px 30px rgba(0,0,0,0.55);
  }

  /* Back side */
  .card-back {
    left: 60px; top: 110px;
    background: var(--card-dark);
  }
  .card-back .wordmark {
    position: absolute; left: 0; right: 0; top: 118px;
    display: flex; align-items: center; justify-content: center; gap: 14px;
  }
  .wordmark-square {
    width: 22px; height: 22px; background: var(--teal);
  }
  .card-back .wordmark-name {
    color: var(--white);
    font-size: 38px; font-weight: 600; letter-spacing: 0.5px;
    text-transform: uppercase;
  }
  .card-back .web-row {
    position: absolute; left: 30px; right: 30px; bottom: 34px;
    display: flex; align-items: center; gap: 16px;
  }
  .card-back .web-row svg { flex: 1; height: 6px; }
  .card-back .web {
    color: var(--teal); font-size: 17px; letter-spacing: 1.2px;
  }

  /* Front side */
  .card-front {
    left: 600px; top: 460px;
    background: var(--card-light);
  }
  .card-front .wordmark {
    position: absolute; right: 34px; top: 44px;
    display: flex; align-items: center; gap: 10px;
  }
  .card-front .wordmark-square { width: 16px; height: 16px; }
  .card-front .wordmark-name {
    color: var(--ink);
    font-size: 28px; font-weight: 600; letter-spacing: 0.3px;
    text-transform: uppercase;
  }
  .contact {
    position: absolute; left: 36px; bottom: 34px;
    color: var(--ink); font-size: 15px; line-height: 1.35;
  }
  .contact .name {
    color: var(--teal); font-size: 24px; font-weight: 700; line-height: 1.1;
  }
  .contact .role { font-size: 16px; margin-bottom: 22px; }
  .contact .label { color: var(--teal); font-weight: 700; }
</style>
</head>
<body>
<main class="canvas">

  <section class="card card-back" aria-label="Card back">
    <div class="wordmark">
      <span class="wordmark-square"></span>
      <span class="wordmark-name">Harvest Lane Estates</span>
    </div>
    <div class="web-row">
      <svg viewBox="0 0 100 6" preserveAspectRatio="none" aria-hidden="true">
        <polygon points="0,6 100,0 100,6" fill="var(--teal)"/>
      </svg>
      <span class="web">www.harvestlaneestates.com.au</span>
      <svg viewBox="0 0 100 6" preserveAspectRatio="none" aria-hidden="true">
        <polygon points="0,0 100,6 0,6" fill="var(--teal)"/>
      </svg>
    </div>
  </section>

  <section class="card card-front" aria-label="Card front">
    <div class="wordmark">
      <span class="wordmark-square"></span>
      <span class="wordmark-name">Harvest Lane Estates</span>
    </div>
    <div class="contact">
      <p class="name">Tom Carrick</p>
      <p class="role">Director/Property Manager</p>
      <p class="address">Level 2, 17 Wattlecourt Rd, Dunmarra NSW 2187</p>
      <p class="lines"><span class="label">P</span>: 0467 239 018 <span class="label">E</span>: tom@harvestlaneestates.com.au</p>
      <p class="web">www.harvestlaneestates.com.au</p>
    </div>
  </section>

</main>
</body>
</html>
```